Modern Design Business Card industrial maintenance company

Business card design for Company named Brookvale Equipment Services

Target Market(s)

Industrial

Industry/Entity Type

Maintenance and repair

Contact Information for Business Card

Place holder for address, office phone, mobile number and email

Requirements
Must have
• Clean modern look
Nice to have
• N/a

```html
<!DOCTYPE html>
<html lang="en">
<head>
<meta charset="utf-8">
<title>Brookvale Equipment Services – Business Card</title>
<link rel="stylesheet" href="https://fonts.googleapis.com/css2?family=Montserrat:wght@500;600&family=Open+Sans:wght@400;700&display=swap">
<style>
  :root {
    --backdrop: #d9d6d1;
    --card-black: #0b0b0b;
    --card-black-soft: #232323;
    --card-white: #ffffff;
    --card-white-soft: #e9e9e9;
    --ink: #141414;
    --ink-muted: #3a3a3a;
    --paper-text: #f2f2f2;
  }
  * { box-sizing: border-box; margin: 0; padding: 0; }
  html, body {
    width: 1200px; height: 1023px; overflow: hidden;
    background: var(--backdrop);
  }
  .canvas { position: relative; width: 1200px; height: 1023px; }

  .card {
    position: absolute;
    width: 640px; height: 366px;
    border-radius: 4px;
    box-shadow: 0 10px 28px rgba(0,0,0,0.25);
  }

  /* Front side */
  .card-front {
    left: 80px; top: 100px;
    background: radial-gradient(ellipse at 40% 40%, var(--card-black-soft), var(--card-black) 70%);
    overflow: hidden;
  }
  .front-texture {
    position: absolute; inset: 0;
    background: linear-gradient(135deg, rgba(255,255,255,0.04), rgba(255,255,255,0) 60%);
  }
  .front-brand {
    position: absolute; left: 0; right: 0; top: 50%;
    transform: translateY(-50%);
    display: flex; align-items: center; justify-content: center; gap: 18px;
  }
  .brand-mark {
    width: 62px; height: 62px; border-radius: 50%;
    border: 3px solid currentColor; flex: none;
  }
  .front-brand { color: var(--paper-text); }
  .brand-name {
    font-family: "Montserrat", sans-serif;
    font-weight: 600; font-size: 25px;
    letter-spacing: 0.06em; text-transform: uppercase;
  }

  /* Back side */
  .card-back {
    left: 480px; top: 560px;
    background: linear-gradient(160deg, var(--card-white) 40%, var(--card-white-soft));
    color: var(--ink);
  }
  .back-brand {
    position: absolute; left: 40px; top: 44px;
    display: flex; align-items: center; gap: 18px;
  }
  .back-brand .brand-mark { width: 92px; height: 92px; border-width: 4px; }
  .back-brand .brand-name { font-size: 24px; }

  .contact-list {
    position: absolute; left: 40px; top: 168px;
    list-style: none;
    font-family: "Open Sans", sans-serif; font-size: 15px; line-height: 1.55;
    color: var(--ink-muted);
  }
  .contact-list li { display: flex; align-items: flex-start; gap: 10px; }
  .contact-list svg { width: 14px; height: 14px; margin-top: 4px; flex: none; }
  .contact-list .address { padding-left: 24px; }

  .holder {
    position: absolute; right: 40px; bottom: 40px; text-align: right;
    font-family: "Open Sans", sans-serif;
  }
  .holder-name { font-weight: 700; font-size: 21px; color: var(--ink); }
  .holder-role { font-size: 14px; color: var(--ink-muted); }
</style>
</head>
<body>
<main class="canvas">

  <section class="card card-front" aria-label="Business card front">
    <div class="front-texture" role="img" aria-label="Faint repeating brand pattern on black"></div>
    <div class="front-brand">
      <span class="brand-mark" aria-hidden="true"></span>
      <span class="brand-name">Brookvale Equipment Services</span>
    </div>
  </section>

  <section class="card card-back" aria-label="Business card back">
    <div class="back-brand">
      <span class="brand-mark" aria-hidden="true"></span>
      <span class="brand-name">Brookvale<br>Equipment Services</span>
    </div>

    <ul class="contact-list">
      <li class="address">418 Millbrook Way,<br>#200 Ashford, Ohio 43015</li>
      <li>
        <svg viewBox="0 0 16 16" aria-hidden="true"><path fill="currentColor" d="M4 1l3 3-2 2c1 2 3 4 5 5l2-2 3 3-2 3C7 15 1 9 1 3z"/></svg>
        (614) 555-0182
      </li>
      <li>
        <svg viewBox="0 0 16 16" aria-hidden="true"><rect x="4" y="1" width="8" height="14" rx="1.5" fill="none" stroke="currentColor" stroke-width="1.5"/><circle cx="8" cy="12.5" r="0.9" fill="currentColor"/></svg>
        (614) 555-0182
      </li>
      <li>
        <svg viewBox="0 0 16 16" aria-hidden="true"><rect x="1" y="3" width="14" height="10" fill="none" stroke="currentColor" stroke-width="1.5"/><path d="M1 3l7 6 7-6" fill="none" stroke="currentColor" stroke-width="1.5"/></svg>
        youremail@youremail.com
      </li>
      <li>
        <svg viewBox="0 0 16 16" aria-hidden="true"><circle cx="8" cy="8" r="6.5" fill="none" stroke="currentColor" stroke-width="1.5"/><path d="M1.5 8h13M8 1.5c-3 3.5-3 9.5 0 13M8 1.5c3 3.5 3 9.5 0 13" fill="none" stroke="currentColor" stroke-width="1.2"/></svg>
        www.yourwebsite.com
      </li>
    </ul>

    <div class="holder">
      <p class="holder-name">Your Name Here</p>
      <p class="holder-role">Managing Director</p>
    </div>
  </section>

</main>
</body>
</html>
```